Referral Card thats different from the rest

Business card size-

Referral card that will be given to clients, in turn they will pass it on to their friends.

The referee will add their name and address, and friends name to card before it is passed on

Referee gets 2 FREE movie tickets

Friend gets $25 OFF their service

Company is an electrical contracting company specialising in the domestic market.

I would like the card to be fun not so serious!
Completely open minded to any and every creative idea!

attached is 2 photo of an example of what another business has, i am trying to achieve something similiar
Updates

I have increased the budget, ;)

i have added 2 x photos of what i am trying to achieve. this is from another business, I am after something similar to this
Thanks

I have updated the design brief.
this should help make it easir and more clear
Thanks

Target Market(s)

Home owners from 30yrs +

Industry/Entity Type

Electrical

Requirements
Must have
• Logo - Not a main feature of card
1300 846 572 on both sides
Lic no: 418695D (doesn’t have to be big) prefer on back

The main feature of the front of the card is the 2 free movie tickets for Referee & $25 OFF Friends first bill

HOW ABOUT TWO FREE MOVIE TICKETS?
It is easy! Know someone who needs an electrician? Maybe a friend, family member, relative or work colleague.
Tell them about us, and we will take $25 off their first bill and give you two FREE Movie Tickets just for introducing us.
To make a referral fill out this card and give it to your friend.

Recommended By:____________
Address:__________________
Frinds name: _____________

*this offer is only valued for work over $55. Non transferable for cash. This coupon is limited to 1 per customer, not to be used in conjunction with any other offer
Nice to have
• Catchy heading on card
example- tell a friend for cash card, (if i was giving away cash vouchers..)

example- keep me in your wallet and pass me on

```html
<!DOCTYPE html>
<html lang="en">
<head>
<meta charset="utf-8">
<title>Bright Spark Electrical – Referral Card</title>
<link rel="stylesheet" href="https://fonts.googleapis.com/css2?family=Lobster&family=Lora:wght@400;700&display=swap">
<style>
  :root {
    --page-bg: #e8e8e8;
    --card-bg: #ffffff;
    --orange: #eea35d;
    --green: #1c8a3c;
    --maroon: #7b2b1f;
    --mascot-blue: #a9d6ef;
    --script: "Lobster", cursive;
    --serif: "Lora", Georgia, serif;
  }
  * { box-sizing: border-box; margin: 0; padding: 0; }
  html, body { width: 871px; height: 1200px; overflow: hidden; }
  body { background: var(--page-bg); position: relative; font-family: var(--serif); }

  .card {
    position: absolute;
    left: 9px;
    width: 857px;
    background: var(--card-bg);
    overflow: hidden;
  }
  .card--front { top: 43px; height: 514px; }
  .card--back { top: 664px; height: 528px; }

  .card__swoosh { position: absolute; inset: 0; width: 100%; height: 100%; }
  .card__swoosh path { fill: var(--orange); }

  .line { position: absolute; line-height: 1; white-space: nowrap; }

  /* front */
  .mascot {
    position: absolute; left: 372px; top: 8px; width: 222px; height: 200px;
    border-radius: 50% 50% 40% 40%;
    background: radial-gradient(circle at 70% 25%, var(--mascot-blue) 0 22%, transparent 23%),
                radial-gradient(circle at 40% 60%, #2f8f4a 0 30%, #e06a2c 31% 45%, transparent 46%);
  }
  .brand {
    left: 312px; top: 236px;
    display: flex; align-items: center; gap: 8px;
    font-weight: 700; font-size: 19px; color: var(--maroon);
  }
  .brand__dot { width: 18px; height: 18px; border-radius: 50%; background: var(--green); }
  .headline {
    left: 0; width: 857px; top: 292px; text-align: center;
    font-family: var(--script); font-weight: 400; font-size: 64px; color: var(--green);
    transform: translateX(20px);
  }
  .front-phone {
    left: 0; width: 857px; top: 361px; text-align: center;
    font-size: 33px; color: var(--maroon);
    transform: translateX(-4px);
  }
  .front-offer {
    left: 0; width: 857px; top: 405px; text-align: center;
    font-size: 18px; color: var(--maroon);
  }
  .front-offer strong { font-weight: 700; }
  .i-am {
    left: 119px; top: 438px;
    font-family: var(--script); font-size: 37px; color: var(--green);
    display: flex; align-items: flex-end; gap: 12px;
  }
  .i-am__blank { display: inline-block; width: 500px; border-bottom: 2px solid var(--green); height: 28px; }

  /* back */
  .referred-title {
    left: 0; width: 857px; top: 24px; text-align: center;
    font-family: var(--script); font-weight: 400; font-size: 36px; color: var(--green);
    transform: translateX(4px);
  }
  .field { left: 242px; font-size: 24px; color: var(--green); display: flex; align-items: flex-end; }
  .field__blank { display: inline-block; border-bottom: 1.5px solid var(--green); height: 22px; }
  .field--name { top: 70px; }
  .field--name .field__blank { width: 276px; margin-left: 6px; }
  .field--address { top: 110px; }
  .field--address .field__blank { width: 276px; }
  .field--friend { top: 150px; }
  .field--friend .field__blank { width: 212px; margin-left: 6px; }

  .pitch {
    left: 0; width: 857px; top: 228px; text-align: center;
    font-size: 22.5px; line-height: 32px; color: var(--maroon); white-space: normal;
  }
  .pitch strong { font-weight: 700; }

  .call {
    left: 0; width: 857px; top: 346px; text-align: center;
    transform: translateX(-23px);
  }
  .call__label { font-family: var(--script); font-size: 41px; color: var(--green); margin-right: 10px; }
  .call__number { font-size: 34px; color: var(--maroon); }

  .licence {
    left: 0; width: 857px; top: 404px; text-align: center;
    transform: translateX(-27px);
  }
  .licence__label { font-family: var(--script); font-size: 30px; color: var(--green); margin-right: 8px; }
  .licence__number { font-size: 28px; color: var(--maroon); }

  .terms {
    left: 14px; width: 780px; top: 470px;
    font-size: 14.5px; line-height: 23px; color: var(--green); white-space: normal;
  }
</style>
</head>
<body>

  <section class="card card--front">
    <svg class="card__swoosh" viewBox="0 0 600 360" preserveAspectRatio="none" aria-hidden="true">
      <path d="M452,0 C405,45 360,115 305,165 C240,225 150,250 104,360 L600,360 L600,0 Z"/>
    </svg>
    <div class="mascot" role="img" aria-label="Cartoon superhero electrician mascot holding up a light bulb"></div>
    <div class="line brand"><span class="brand__dot"></span>Bright Spark Electrical Pty Ltd</div>
    <h1 class="line headline">We are the Live Wires!</h1>
    <p class="line front-phone">1300 846 572</p>
    <p class="line front-offer">You get 2 <strong>FREE</strong> movie tickets &amp; your friend gets <strong>$25 OFF</strong></p>
    <p class="line i-am">I am <span class="i-am__blank"></span></p>
  </section>

  <section class="card card--back">
    <svg class="card__swoosh" viewBox="0 0 600 360" preserveAspectRatio="none" aria-hidden="true">
      <path d="M448,0 C385,40 345,105 333,170 C315,262 150,280 98,360 L600,360 L600,0 Z"/>
    </svg>
    <h2 class="line referred-title">I was referred by</h2>
    <p class="line field field--name">Name:<span class="field__blank"></span></p>
    <p class="line field field--address">Address:<span class="field__blank"></span></p>
    <p class="line field field--friend">Friend’s name:<span class="field__blank"></span></p>

    <p class="line pitch">If you’re happy with our service, we would really love for you to recommend<br>
      us to your friends.If your friends use our service we will give you<br>
      2 <strong>FREE</strong> movie tickets &amp; your friends <strong>$25</strong> OFF their service.</p>

    <p class="line call"><span class="call__label">Call now on</span><span class="call__number">1300 846 572</span></p>
    <p class="line licence"><span class="licence__label">Lic Number</span><span class="licence__number">418695D</span></p>

    <p class="line terms">*this offer is only valued for work over $55. Non transferable for cash. This coupon is limited to 1 per customer,not to be used in conjunction with any other offer.</p>
  </section>

</body>
</html>
```